Wordpress Site Design for a Horror and Action Movie Production Company

We need a re-design/facelift of our website: https://qz7v.pagebuild.io
The structure of the website could remain the same, but it needs to look and feel BETTER!

We would like the website coded in Wordpress so that it can be easily updated bu us, via adding new projects and new projects' info.

We specialize in Action, Horror, and Sci-Fi Genre. That being said, we don't want the website to look like it's a themed park with haunted houses. It should still be sharp and professional, as after all - it is a business for us!

Target Market(s)

Film Distribution Companies (B2B), as well as general audience that likes movies

Industry/Entity Type

Movie Production

Coding

Coded - Design and coding required

Number of Pages Required

5+ page

Font styles to use
Sans Serif

Colors

Designer to choose colors to be used in the design.

Requirements
Must have
• - PROJECTS page
• - Each PROJECT has a sub-page with project info/updates (up dates could be in a form of a WP post, ideally a template that we can use to update and create new PROJECT pages, with text, poster, and video link (trailer))
• - NEWS page that chronologically lists updates from all PROJECTS (could be done via WP blog)
• - HOME page would
Nice to have
• Should generally have a dark background.
• Websites we like as a reference of general approach and style:
• https://marrowlane.com
• https://velkastudio.com (however this is very image-centric, and we might not have that much imagery at the moment)
• https://www.briarpeakpicturehouse.com/other
• https://quellfilms.com
Should not have
• We specialize in Action, Horror, and Sci-Fi Genre. That being said, we don't want the website to look like it's a themed park with haunted houses. It should still be sharp and professional, as after all - it is a business for us!

```html
<!DOCTYPE html>
<html lang="en">
<head>
<meta charset="utf-8">
<title>Outpost 27 Media</title>
<link rel="stylesheet" href="https://fonts.googleapis.com/css2?family=Montserrat:wght@500;600;700&family=Poppins:wght@700&family=Lato:wght@400;700&display=swap">
<style>
:root{
  --nav:#231f20;
  --black:#050505;
  --panel:#1b1a1a;
  --card:#0c0c0c;
  --red:#e0261c;
  --red-line:#b3201a;
  --white:#ffffff;
  --muted:#d7d7d7;
  --ghost:rgba(255,255,255,0.06);
}
*{margin:0;padding:0;box-sizing:border-box}
html,body{width:1200px;height:3531px;overflow:hidden;background:var(--panel)}
body{position:relative;font-family:"Lato",sans-serif;color:var(--white)}
.abs{position:absolute}
.center{left:0;width:1200px;text-align:center}

/* nav */
.site-nav{left:0;top:0;width:1200px;height:110px;background:var(--nav);z-index:5}
.brand{left:143px;top:38px;font-family:"Montserrat",sans-serif;font-weight:600;font-size:24px;letter-spacing:1px}
.menu{left:454px;top:46px;display:flex;gap:29px;font-family:"Montserrat",sans-serif;font-weight:500;font-size:13px}
.menu .active{color:var(--red)}
.nav-divider{left:903px;top:30px;width:1px;height:52px;background:#3a3637}
.socials{display:flex;gap:8px}
.socials span{width:26px;height:26px;border:1.5px solid #fff;border-radius:50%;display:block}

/* hero */
.hero{left:0;top:110px;width:1200px;height:560px;background:radial-gradient(ellipse at 58% 35%,#6b5a55 0%,#3a3230 35%,#1d1a1a 70%,#0e0d0d 100%)}
.hero-title{top:472px;font-family:"Poppins",sans-serif;font-weight:700;font-size:38px;line-height:48px}

/* curved bands */
.band-black{background:var(--black)}
.about-band{left:-300px;top:596px;width:1800px;height:520px;border-radius:50%/110px}
.projects-band{left:-300px;top:1668px;width:1800px;height:860px;border-radius:50%/110px}
.footer-band{left:-300px;top:3190px;width:1800px;height:500px;border-radius:50%/90px}

.section-title{font-family:"Montserrat",sans-serif;font-weight:600;font-size:28px}
.ghost{font-family:"Montserrat",sans-serif;font-weight:600;font-size:54px;color:var(--ghost);letter-spacing:1px}

.about-text{left:160px;width:880px;text-align:center;font-size:13.5px;line-height:24px}
.partner{width:410px;display:flex;gap:18px}
.partner-mark{width:110px;height:60px;display:flex;align-items:center;justify-content:center;flex-shrink:0}
.partner-mark span{width:40px;height:40px;background:#e9e9e9;display:block}
.partner h3{font-family:"Montserrat",sans-serif;font-weight:600;font-size:15px;margin-bottom:8px}
.partner p{font-size:11.5px;line-height:17px;color:var(--muted)}

.btn{width:133px;height:44px;border:1.5px solid var(--red);box-shadow:0 0 10px rgba(224,38,28,.45);display:flex;align-items:center;justify-content:center;font-family:"Montserrat",sans-serif;font-weight:600;font-size:12.5px;background:var(--black)}

/* genres */
.genre{width:281px;height:298px;border:1.5px solid #444;background:var(--panel)}
.genre.featured{border-color:var(--red);box-shadow:0 0 14px rgba(224,38,28,.5)}
.genre .media{position:absolute;left:7px;top:7px;width:264px;height:226px}
.genre .label{position:absolute;left:0;top:252px;width:100%;text-align:center;font-family:"Montserrat",sans-serif;font-weight:600;font-size:18px}

/* projects */
.project{overflow:hidden}
.project .frame{position:absolute;inset:10px;border:1.5px solid var(--red-line)}
.project .name{position:absolute;left:0;width:100%;text-align:center;font-family:"Montserrat",sans-serif;font-weight:600;font-size:20px;z-index:2}
.project .ghost-name{position:absolute;left:-40px;right:-40px;text-align:center;font-family:"Montserrat",sans-serif;font-weight:600;font-size:44px;color:rgba(255,255,255,.12);white-space:nowrap}

/* news */
.news{width:282px;height:368px;background:var(--card)}
.news .media{height:214px}
.news .date{position:absolute;left:17px;top:248px;height:32px;padding:0 14px;display:flex;align-items:center;font-size:13px;background:#fff;color:var(--red)}
.news .date.hot{background:var(--red);color:#fff}
.news h4{position:absolute;left:17px;top:296px;width:250px;font-family:"Montserrat",sans-serif;font-weight:600;font-size:15px;line-height:22px}

/* footer */
.legal{left:150px;width:900px;text-align:center;font-size:10.5px;line-height:19px}
.legal strong{display:block;font-weight:700;margin:6px 0 2px}
.footer-rule{left:143px;top:3480px;width:915px;height:1px;background:#2a2a2a}
.copyright{left:143px;top:3496px;font-size:12.5px}
</style>
</head>
<body>

<header class="abs site-nav">
  <div class="abs brand">OUTPOST 27 MEDIA</div>
  <nav class="abs menu">
    <span class="active">HOME</span><span>ABOUT US</span><span>NEWS</span><span>PROJECTS</span><span>CONTACT US</span>
  </nav>
  <div class="abs nav-divider"></div>
  <div class="abs socials" style="left:929px;top:42px" aria-label="Social links"><span></span><span></span><span></span><span></span></div>
</header>

<section class="abs hero" role="img" aria-label="Horror film still: a screaming woman grabbed by a group of zombies in a dark corridor"></section>
<h1 class="abs center hero-title">We specialize in Action, Horror, and<br>Sci-Fi Genre.</h1>

<!-- about -->
<div class="abs band-black about-band"></div>
<div class="abs center ghost" style="top:686px">ABOUT OUTPOST 27 MEDIA</div>
<h2 class="abs center section-title" style="top:705px">ABOUT OUTPOST 27 MEDIA</h2>
<p class="abs about-text" style="top:766px">Outpost 27 Media Inc (O27M) is a fresh brand of multi-media Visual Content, aimed at development of original Canadian content as well as servicing of foreign productions here at home, in Ontario, Canada.</p>
<p class="abs about-text" style="top:824px">O27M is a child of a partnership between two Canadian companies, which for years have been rec-ognized as key brands in the Canadian media landscape:</p>

<div class="abs partner" style="left:152px;top:884px">
  <div class="partner-mark"><span></span></div>
  <div><h3>Crowline Pictures Inc</h3><p>Crowline Pictures is led by partners Daniel Orvik, Peter Lusk and Simon Vey. It represents unique, innovative and cutting edge genre films for...[+]</p></div>
</div>
<div class="abs partner" style="left:616px;top:884px">
  <div class="partner-mark"><span></span></div>
  <div><h3>Lumen Six Entertainment Inc</h3><p>Crowline Pictures is led by partners Daniel Orvik, Peter Lusk and Simon Vey. It represents unique, innovative and cutting edge genre films for North...[+]</p></div>
</div>
<div class="abs btn" style="left:533px;top:1005px">READ MORE</div>

<!-- specialize -->
<div class="abs center ghost" style="top:1195px">WE SPECIALIZE IN</div>
<h2 class="abs center section-title" style="top:1217px">WE SPECIALIZE IN</h2>
<div class="abs genre featured" style="left:141px;top:1286px"><div class="media" role="img" aria-label="Action film still: police officer shielding people on a dark street" style="background:linear-gradient(160deg,#4a4b4a,#222323 60%,#131313)"></div><div class="label">ACTION</div></div>
<div class="abs genre" style="left:459px;top:1286px"><div class="media" role="img" aria-label="Horror film still: pale possessed girl in a bedroom" style="background:linear-gradient(160deg,#7a6e66,#56504f 55%,#3b3737)"></div><div class="label">HORROR</div></div>
<div class="abs genre" style="left:777px;top:1286px"><div class="media" role="img" aria-label="Sci-fi film still: armoured figure walking through a glowing doorway" style="background:radial-gradient(ellipse at 55% 40%,#e0a55a,#8a5b2c 40%,#2a2620 80%)"></div><div class="label">SCI-FI GENRE</div></div>

<!-- projects -->
<div class="abs band-black projects-band"></div>
<div class="abs center ghost" style="top:1752px">RECENT PROJECTS</div>
<h2 class="abs center section-title" style="top:1772px">RECENT PROJECTS</h2>

<div class="abs project" style="left:141px;top:1844px;width:283px;height:239px" role="img" aria-label="Still from Neon Drifter: young hero in a dark wasteland">
  <div class="abs" style="inset:0;background:linear-gradient(150deg,#3c3a38,#222 60%,#171717)"></div>
  <div class="frame"></div><div class="ghost-name" style="top:96px">NEON DRIFTER</div><div class="name" style="top:106px">NEON DRIFTER</div>
</div>
<div class="abs project" style="left:465px;top:1844px;width:282px;height:239px" role="img" aria-label="Still from Gone Too Deep: woman in a dim room">
  <div class="abs" style="inset:0;background:linear-gradient(150deg,#2a2c30,#1d1f24 60%,#141518)"></div>
  <div class="frame"></div><div class="ghost-name" style="top:96px">GONE TOO DEEP</div><div class="name" style="top:106px">GONE TOO DEEP</div>
</div>
<div class="abs project" style="left:784px;top:1844px;width:274px;height:517px" role="img" aria-label="Still from Dark Current: man in a shadowy interior">
  <div class="abs" style="inset:0;background:linear-gradient(170deg,#141416,#241c18 45%,#120f0e)"></div>
  <div class="frame"></div><div class="ghost-name" style="top:236px">DARK CURRENT</div><div class="name" style="top:246px">DARK CURRENT</div>
</div>
<div class="abs project" style="left:141px;top:2121px;width:606px;height:240px" role="img" aria-label="Still from Aurora Line: driver inside a car at night">
  <div class="abs" style="inset:0;background:linear-gradient(160deg,#2c2c2c,#1a1a1a 55%,#101010)"></div>
  <div class="frame"></div><div class="ghost-name" style="top:96px">AURORA LINE</div><div class="name" style="top:106px">AURORA LINE</div>
</div>
<div class="abs btn" style="left:533px;top:2397px">VIEW ALL</div>

<!-- news -->
<div class="abs center ghost" style="top:2586px">LATEST NEWS</div>
<h2 class="abs center section-title" style="top:2606px">LATEST NEWS</h2>
<article class="abs news" style="left:141px;top:2665px"><div class="media" role="img" aria-label="News image: astronaut lit by blue light" style="background:radial-gradient(ellipse at 45% 40%,#7fb4e8,#2b5a96 45%,#0f1d33)"></div><div class="date hot">15 Oct 2019</div><h4>LOREM IPSM DOOR SIT CONSER ADIPISCING ELIT SED DIAM.</h4></article>
<article class="abs news" style="left:459px;top:2665px"><div class="media" role="img" aria-label="News image: girl asleep beside a creepy doll" style="background:linear-gradient(150deg,#3b8fa8,#2a4f6a 50%,#3a2434)"></div><div class="date">15 Oct 2019</div><h4>LOREM IPSM DOOR SIT CONSER ADIPISCING ELIT SED DIAM.</h4></article>
<article class="abs news" style="left:777px;top:2665px"><div class="media" role="img" aria-label="News image: two men running through a dusty town" style="background:linear-gradient(160deg,#a8a296,#7a6f5e 50%,#4d4438)"></div><div class="date">15 Oct 2019</div><h4>LOREM IPSM DOOR SIT CONSER ADIPISCING ELIT SED DIAM.</h4></article>
<div class="abs btn" style="left:533px;top:3064px">VIEW ALL</div>

<!-- footer -->
<div class="abs band-black footer-band"></div>
<div class="abs legal" style="top:3272px">
  All the information on this website is published in good faith and for general information purpose only. Outpost 27 Media Inc. does not make any warranties about the completeness, reliability and accuracy of this information. Any action you take upon the information you find on this website is strictly at your own risk. will not be liable for any losses and/or damages in connection with the use of our website.
  <strong>SCRIPT AND STORY SUBMISSION NOTICE</strong>
  Any unsolicited pitches, outlines, scripts, treatments, etc. will be discarded and will not be read. The purpose of this policy is to avoid any potential misunderstandings if your original work seems similar to something we may already have in development. Please note, if you choose to submit materials regardless of this policy, you acknowledge that you have read our submission policy and understand that by making such a submission, you understand that Outpost 27 Media Inc. has no obligation to you or your submission and that you have no claim whatsoever based on such submission.
</div>
<div class="abs footer-rule"></div>
<div class="abs copyright">Copyright © 2019 Outpost 27 Media Inc. All Rights Reserved</div>
<div class="abs socials" style="left:929px;top:3490px" aria-label="Social links"><span></span><span></span><span></span><span></span></div>

</body>
</html>
```